International Trading Company, 'KIRO' needs a Business Card

The company name is "KIRO" and it has own logo design.
I'd like to use its logo on this business card.
I need two side Business Card.
I'll look forward to your great design.
Thank you very much in advance.

Contact Information for Business Card

Company Name : Kiro Harbour Limited
Information Example
Dorian Pallister
Mobile(use icon please) : 1 (212) 555-0143
Tel(use icon please) : 1 (212) 555-0178
Email(use icon please) : dorian27@kiroharbour-mail.com
Address(use icon please) : 482 Halden Ave, New York, NY 10160, USA

```html
<!DOCTYPE html>
<html lang="en">
<head>
<meta charset="utf-8">
<title>KIRO – Business Card</title>
<link rel="stylesheet" href="https://fonts.googleapis.com/css2?family=Open+Sans:wght@400;600;700&display=swap">
<style>
  :root {
    --canvas: #e9e9ea;
    --charcoal: #3a3a3c;
    --white: #ffffff;
    --sky: #38b6e6;
    --ocean: #1c8fc0;
    --mist: #8fd2ee;
    --ink: #4a4a4c;
  }
  html, body {
    margin: 0;
    padding: 0;
    width: 1200px;
    height: 1200px;
    overflow: hidden;
    background: var(--canvas);
  }
  .sheet {
    width: 1200px;
    height: 1200px;
    display: flex;
    flex-direction: column;
    align-items: center;
    justify-content: center;
    gap: 44px;
  }
  .card {
    width: 900px;
    height: 518px;
    box-shadow: 0 14px 30px rgba(0,0,0,0.22);
    background: var(--charcoal);
  }
  .card svg { display: block; width: 100%; height: 100%; }
  .bg-dark { fill: var(--charcoal); }
  .panel-white { fill: var(--white); }
  .band-sky { fill: var(--sky); }
  .band-ocean { fill: var(--ocean); }
  .pattern-area { fill: url(#pattern-tone); }
  .brand-name {
    font-family: "Open Sans", sans-serif;
    font-weight: 700;
    fill: var(--ink);
    letter-spacing: 1px;
  }
  .holder-name {
    font-family: "Open Sans", sans-serif;
    font-weight: 600;
    font-size: 12.5px;
    fill: var(--white);
  }
  .contact-line {
    font-family: "Open Sans", sans-serif;
    font-weight: 400;
    font-size: 8.4px;
    fill: var(--white);
  }
  .strip-line {
    font-family: "Open Sans", sans-serif;
    font-weight: 400;
    font-size: 7px;
    fill: var(--white);
  }
  .icon-box { fill: var(--sky); }
  .icon-glyph { fill: var(--white); }
  .icon-stroke { fill: none; stroke: var(--white); stroke-width: 0.9; }
</style>
</head>
<body>
<main class="sheet">

  <section class="card card-front" aria-label="Business card front">
    <svg viewBox="0 0 426 245" preserveAspectRatio="none">
      <defs>
        <linearGradient id="pattern-tone" x1="0" y1="0" x2="1" y2="1">
          <stop offset="0" stop-color="#38b6e6"/>
          <stop offset="0.55" stop-color="#8fd2ee"/>
          <stop offset="1" stop-color="#1c8fc0"/>
        </linearGradient>
      </defs>

      <rect class="bg-dark" width="426" height="245"/>
      <g role="img" aria-label="Blue geometric mosaic decoration">
        <polygon class="pattern-area" points="250,150 282,150 306,245 212,245"/>
      </g>
      <polygon class="band-ocean" points="214,0 234,0 222,20"/>
      <polygon class="band-sky" points="232,0 300,0 245,98 276,170 260,178 205,98"/>
      <polygon class="panel-white" points="300,0 426,0 426,245 305,245 245,98"/>

      <text class="brand-name" x="346" y="137" font-size="42" text-anchor="middle">KIRO</text>

      <rect class="icon-box" x="18" y="54" width="11" height="11"/>
      <circle class="icon-glyph" cx="23.5" cy="58" r="2"/>
      <path class="icon-glyph" d="M20 63.5 Q23.5 59.5 27 63.5 Z"/>
      <text class="holder-name" x="37" y="64.5">Dorian Pallister</text>

      <rect class="icon-box" x="18" y="92" width="11" height="11"/>
      <rect class="icon-stroke" x="21.5" y="94" width="4" height="7" rx="0.6"/>
      <text class="contact-line" x="37" y="100.5">1 (212) 555-0143</text>

      <rect class="icon-box" x="18" y="117" width="11" height="11"/>
      <path class="icon-glyph" d="M20.5 119.5 L22.5 119 L23.5 121.3 L22.4 122.2 Q23.3 124 24.9 124.7 L25.8 123.6 L28 124.6 L27.5 126.5 Q22 126 20.5 119.5 Z"/>
      <text class="contact-line" x="37" y="125.5">1 (212) 555-0178</text>

      <rect class="icon-box" x="18" y="141" width="11" height="11"/>
      <rect class="icon-stroke" x="20.3" y="143.8" width="6.4" height="5"/>
      <path class="icon-stroke" d="M20.3 143.8 L23.5 146.6 L26.7 143.8"/>
      <text class="contact-line" x="37" y="149.5">dorian27@kiroharbour-mail.com</text>

      <rect class="icon-box" x="18" y="166" width="11" height="11"/>
      <path class="icon-glyph" d="M23.5 175.5 L20.9 171 A3 3 0 1 1 26.1 171 Z"/>
      <circle fill="var(--sky)" cx="23.5" cy="169.8" r="1"/>
      <text class="contact-line" x="37" y="174.5">482 Halden Ave, New York, NY</text>
      <text class="contact-line" x="37" y="185.5">10160, USA</text>
    </svg>
  </section>

  <section class="card card-back" aria-label="Business card back">
    <svg viewBox="0 0 426 245" preserveAspectRatio="none">
      <rect class="bg-dark" width="426" height="245"/>
      <g role="img" aria-label="Blue geometric mosaic decoration">
        <polygon class="pattern-area" points="80,150 112,150 136,245 42,245"/>
      </g>
      <polygon class="band-ocean" points="48,0 66,0 56,18"/>
      <polygon class="band-sky" points="62,0 130,0 75,98 106,170 90,178 35,98"/>
      <polygon class="panel-white" points="130,0 426,0 426,245 135,245 75,98"/>

      <text class="brand-name" x="258" y="140" font-size="58" text-anchor="middle">KIRO</text>

      <rect class="band-sky" x="128" y="216" width="298" height="14"/>
      <rect class="band-ocean" x="131" y="230" width="295" height="2"/>

      <path class="icon-glyph" d="M190 219.5 L191.6 219.1 L192.4 221 L191.5 221.7 Q192.2 223.1 193.5 223.7 L194.2 222.8 L196 223.6 L195.6 225.1 Q191.2 224.8 190 219.5 Z"/>
      <text class="strip-line" x="199" y="225.6">1 (212) 555-0178</text>

      <rect class="icon-stroke" x="286" y="220" width="6" height="4.6"/>
      <path class="icon-stroke" d="M286 220 L289 222.6 L292 220"/>
      <text class="strip-line" x="296" y="225.6">dorian27@kiroharbour-mail.com</text>
    </svg>
  </section>

</main>
</body>
</html>
```